Media Browser and player web application

I need to redesign a web application that enables to browse a media server (Lumarra) contents (images, audio, video) and play it in a web player.

Current implementation of the application can be seen at: http://www.kelbofaq.net/content/demonstration-lumarra-pro-online-media-browser

This refresh is aiming to:
1) make the application simpler, based on typology (think Panelix Tile style, VidHalo, Flickro); a simple fan concept is here: http://tow.gandeliq.net/lumarra/
2) make the application work on desktop as well as touch screen devices (ie no hover functionality, no pagination, large touch controls)
3) fast (remove unnecessary animations)
4) design with the app being responsive in mind

The attached UX designs show the basic flows in the application. Please note that the placement of controls (for example) is not set in stone and I welcome your input on the layout.

Ideally the default theme will be dark. Items' thumbnails will be square place holders, with images fit in them depending on the item icons' aspect ratio.

Also attaching the product's logo (Lumarra) and icon. The web application's name is ClipRoamer (or Lumarra ClipRoamer), so it should be included in the design (the UX designs include place holder Lumarra logo in the left top corner).

The main categories for each file type are (you will have to provide an icon for each of these):
- Audio: Albums, Artists, Album artists, Folders, Genres, Composers, Titles, Random music, Random albums, Last listened, Playlists, Online
- Image: Albums, Folders, Year, Month, Playlists, Online
- Video: Titles, Movies, Series, Folders, Last viewed, Last added, Genres, Actors, Directors, Producers, Release years, Playlists, Online
Updates

Target Market(s)

Mostly tech enthusiasts who want to stream their media over the internet to their devices.

Industry/Entity Type

Artists

Requirements
Must have
• Designs for all the provided UX designs
Touch-friendly web application design
High-res (Retina) assets
Light, type based Tile-like design
Nice to have
• Responsive web version
Dark and Light theme switching.
Should not have
• Chrome
Heavy graphics (eg backgrounds) that take time to load

```html
<!DOCTYPE html>
<html lang="en">
<head>
<meta charset="utf-8">
<title>ClipRoamer – Video</title>
<link rel="stylesheet" href="https://fonts.googleapis.com/css2?family=Open+Sans:wght@300;400;600;800&display=swap">
<style>
:root{
  --bar:#141414;
  --white:#ffffff;
  --canvas:#6b6b6b;
  --crumb:#a7a7a7;
  --section:#39b4e6;
  --section-tab:#74c9f0;
  --field:#1c1c1c;
  --field-line:#4a4a4a;
  --chip:#3a3a3a;
  --scroll-track:#d7d7d7;
  --scroll-thumb:#ececec;
  --avatar:#b2573f;
  --titles:#a4b81f;
  --movies:#e6b820;
  --series:#e6706a;
  --folders:#7dbcb0;
  --viewed:#1f8f9a;
  --added:#7b4f93;
  --genres:#c9ae93;
  --actors:#b48fc8;
  --directors:#18b8ee;
  --producers:#3a5898;
  --years:#748a72;
  --playlists:#3c3f3a;
  --online:#dd6b3c;
  --nav-images:#f3a21b;
  --nav-audio:#e0262e;
  --nav-video:#2fb2e8;
}
*{box-sizing:border-box;margin:0;padding:0}
html,body{width:1200px;height:753px;overflow:hidden;background:var(--canvas);font-family:"Open Sans",sans-serif}
.app{position:relative;width:1200px;height:753px;overflow:hidden;background:var(--canvas)}

.topbar{position:absolute;left:0;top:0;width:1200px;height:84px;background:var(--bar)}
.brand{position:absolute;left:30px;top:22px;color:var(--white);font-weight:800;font-size:27px;letter-spacing:1px;line-height:40px}
.main-nav{position:absolute;top:33px;left:0;display:flex}
.nav-item{position:absolute;display:flex;align-items:center;gap:8px;color:var(--white);font-size:13px;text-transform:uppercase;white-space:nowrap;text-decoration:none}
.nav-item svg{width:20px;height:18px}
.nav-images{left:245px}
.nav-audio{left:360px}
.nav-video{left:465px}
.search{position:absolute;left:605px;top:29px;width:143px;height:26px;border-radius:13px;background:var(--field);border:1px solid var(--field-line)}
.search svg{position:absolute;right:8px;top:6px;width:13px;height:13px}
.tool{position:absolute;top:30px;width:25px;height:24px;background:var(--chip);border-radius:2px}
.tool svg{position:absolute;left:5px;top:5px;width:15px;height:14px}
.tool-theme{left:826px}
.tool-settings{left:860px}
.avatar{position:absolute;left:1046px;top:20px;width:46px;height:44px;background:linear-gradient(160deg,#c9453a,#9a5a3f 60%,#d99a7a)}
.user-name{position:absolute;left:1107px;top:34px;color:var(--white);font-size:13px;text-transform:uppercase}
.user-more{position:absolute;left:1185px;top:37px;width:10px;height:10px;border-radius:50%;border:1px solid #777}

.subbar{position:absolute;left:0;top:84px;width:1200px;height:54px;background:var(--white)}
.section-title{position:absolute;left:0;top:0;width:190px;height:54px;background:var(--section);color:var(--white);font-weight:300;font-size:30px;line-height:54px;padding-left:31px}
.section-toggle{position:absolute;left:190px;top:0;width:23px;height:54px;background:var(--section-tab)}
.section-toggle svg{position:absolute;left:5px;top:21px;width:12px;height:12px}
.breadcrumb{position:absolute;left:243px;top:19px;font-size:12px;color:var(--crumb);display:flex;gap:12px}
.breadcrumb a{color:var(--crumb);text-decoration:underline}
.queue{position:absolute;left:1140px;top:8px;width:30px;text-align:center;color:#8a8a8a;font-size:8px}
.queue svg{width:26px;height:26px;display:block;margin:0 auto 2px}

.tiles{position:absolute;left:0;top:138px;width:1200px;height:615px}
.tile{position:absolute;width:163px;height:163px;color:var(--white);text-decoration:none}
.tile svg{position:absolute;left:41px;top:20px;width:80px;height:80px}
.tile-label{position:absolute;left:0;right:0;top:111px;text-align:center;font-size:20px;line-height:28px}
.scrollbar{position:absolute;left:1182px;top:168px;width:12px;height:415px;border-radius:6px;background:var(--scroll-track)}
.scrollbar-thumb{position:absolute;left:1px;top:28px;width:10px;height:135px;border-radius:5px;background:var(--scroll-thumb)}
</style>
</head>
<body>
<div class="app">
  <header class="topbar">
    <div class="brand">CLIPROAMER</div>
    <nav class="main-nav">
      <a class="nav-item nav-images" href="#"><svg viewBox="0 0 20 18"><rect x="1" y="1" width="18" height="16" fill="none" stroke="var(--nav-images)" stroke-width="2"/><path d="M4 14l4-5 3 3 2-2 3 4z" fill="var(--nav-images)"/><circle cx="13" cy="6" r="1.6" fill="var(--nav-images)"/></svg>Images</a>
      <a class="nav-item nav-audio" href="#"><svg viewBox="0 0 20 18"><path d="M7 3l11-2v12.5a3 3 0 1 1-2-2.8V5L9 6.3v9.2a3 3 0 1 1-2-2.8z" fill="var(--nav-audio)"/></svg>Audio</a>
      <a class="nav-item nav-video" href="#"><svg viewBox="0 0 20 18"><circle cx="5" cy="4" r="3" fill="var(--nav-video)"/><circle cx="11" cy="4" r="3" fill="var(--nav-video)"/><rect x="1" y="8" width="13" height="8" fill="var(--nav-video)"/><path d="M14 11l5-3v8l-5-3z" fill="var(--nav-video)"/></svg>Video</a>
    </nav>
    <div class="search"><svg viewBox="0 0 13 13"><circle cx="5" cy="5" r="3.8" fill="none" stroke="#fff" stroke-width="1.8"/><path d="M8 8l4 4" stroke="#fff" stroke-width="2"/></svg></div>
    <div class="tool tool-theme"><svg viewBox="0 0 15 14"><circle cx="7.5" cy="7" r="3" fill="none" stroke="#aaa" stroke-width="1.4"/><path d="M7.5 0v2M7.5 12v2M0.5 7h2M12.5 7h2M2.5 2l1.4 1.4M11 10.6l1.4 1.4M2.5 12l1.4-1.4M11 3.4L12.4 2" stroke="#aaa" stroke-width="1.2"/></svg></div>
    <div class="tool tool-settings"><svg viewBox="0 0 15 14"><circle cx="7.5" cy="7" r="4.5" fill="#aaa"/><path d="M7.5 0v14M0.5 7h14M2.5 2l10 10M2.5 12l10-10" stroke="#aaa" stroke-width="2.4"/><circle cx="7.5" cy="7" r="1.8" fill="var(--chip)"/></svg></div>
    <div class="avatar" role="img" aria-label="User profile photo"></div>
    <div class="user-name">Tobin Marsh</div>
    <div class="user-more"></div>
  </header>

  <div class="subbar">
    <div class="section-title">VIDEO</div>
    <div class="section-toggle"><svg viewBox="0 0 12 12"><circle cx="6" cy="6" r="6" fill="#fff"/><path d="M4 6h4M6 4l2 2-2 2" stroke="var(--section-tab)" stroke-width="1.5" fill="none"/></svg></div>
    <div class="breadcrumb"><a href="#">Home</a><span>›</span><a href="#">Video</a></div>
    <div class="queue"><svg viewBox="0 0 26 26"><circle cx="13" cy="13" r="12" fill="none" stroke="#8a8a8a" stroke-width="1.2"/><rect x="8.5" y="8" width="9" height="10" fill="none" stroke="#8a8a8a" stroke-width="1.2"/><path d="M10.5 11h5M10.5 13h5M10.5 15h5" stroke="#8a8a8a"/></svg>Queue</div>
  </div>

  <main class="tiles">
    <a class="tile" href="#" style="left:30px;top:31px;background:var(--titles)"><svg viewBox="0 0 80 80"><rect x="14" y="14" width="10" height="52" fill="#fff"/><path d="M5 20h58l12 11-12 11H5z" fill="#fff"/><rect x="12" y="27" width="30" height="5" fill="var(--titles)"/></svg><span class="tile-label">Titles</span></a>
    <a class="tile" href="#" style="left:225px;top:31px;background:var(--movies)"><svg viewBox="0 0 80 80"><rect x="3" y="12" width="74" height="56" fill="#fff"/><g fill="var(--movies)"><rect x="8" y="17" width="7" height="7"/><rect x="8" y="29" width="7" height="7"/><rect x="8" y="41" width="7" height="7"/><rect x="8" y="53" width="7" height="7"/><rect x="65" y="17" width="7" height="7"/><rect x="65" y="29" width="7" height="7"/><rect x="65" y="41" width="7" height="7"/><rect x="65" y="53" width="7" height="7"/><rect x="20" y="17" width="40" height="46"/></g><path d="M33 28l16 12-16 12z" fill="#fff"/></svg><span class="tile-label">Movies</span></a>
    <a class="tile" href="#" style="left:421px;top:31px;background:var(--series)"><svg viewBox="0 0 80 80"><g fill="none" stroke="#fff" stroke-width="6"><path d="M4 38h6v22M3 60h14"/><path d="M30 24h14v10H30v12h14"/><path d="M54 34h16v12H58M70 46v14H54"/></g></svg><span class="tile-label">Series</span></a>
    <a class="tile" href="#" style="left:616px;top:31px;background:var(--folders)"><svg viewBox="0 0 80 80"><path d="M3 12h22l5 6h36v8H14L3 64z" fill="#fff"/><path d="M14 30h64L68 68H3z" fill="#fff"/></svg><span class="tile-label">Folders</span></a>
    <a class="tile" href="#" style="left:811px;top:31px;background:var(--viewed)"><svg viewBox="0 0 80 80"><path d="M2 35C20 10 60 10 78 35 60 60 20 60 2 35z" fill="#fff"/><circle cx="40" cy="33" r="15" fill="var(--viewed)"/><circle cx="40" cy="33" r="10" fill="#fff"/></svg><span class="tile-label">Last Viewed</span></a>
    <a class="tile" href="#" style="left:1007px;top:31px;background:var(--added)"><svg viewBox="0 0 80 80"><path d="M44 4l30 30-6 4-4-3-16 16 2 12-6 4-24-24 4-6 12 2 16-16-3-4z" fill="#fff"/><path d="M26 52L4 78l26-22z" fill="#fff"/></svg><span class="tile-label">Last Added</span></a>

    <a class="tile" href="#" style="left:30px;top:224px;background:var(--genres)"><svg viewBox="0 0 80 80"><g fill="#fff"><rect x="4" y="4" width="16" height="16"/><rect x="4" y="32" width="16" height="16"/><rect x="4" y="60" width="16" height="16"/><rect x="30" y="8" width="46" height="8"/><rect x="30" y="36" width="46" height="8"/><rect x="30" y="64" width="46" height="8"/></g></svg><span class="tile-label">Genres</span></a>
    <a class="tile" href="#" style="left:225px;top:224px;background:var(--actors)"><svg viewBox="0 0 80 80"><circle cx="40" cy="40" r="34" fill="none" stroke="#fff" stroke-width="6"/><path d="M40 20l6 13 14 1-11 9 4 14-13-8-13 8 4-14-11-9 14-1z" fill="#fff"/></svg><span class="tile-label">Actors</span></a>
    <a class="tile" href="#" style="left:421px;top:224px;background:var(--directors)"><svg viewBox="0 0 80 80"><rect x="16" y="4" width="48" height="20" fill="#fff"/><path d="M40 9l2 4h4l-3 3 1 4-4-2-4 2 1-4-3-3h4z" fill="var(--directors)"/><rect x="14" y="30" width="52" height="7" fill="#fff"/><path d="M20 37l40 40M60 37L20 77" stroke="#fff" stroke-width="7"/><path d="M20 24v10M60 24v10" stroke="#fff" stroke-width="5"/></svg><span class="tile-label">Directors</span></a>
    <a class="tile" href="#" style="left:616px;top:224px;background:var(--producers)"><svg viewBox="0 0 80 80"><path d="M4 24L68 6l3 12L7 36z" fill="#fff"/><path d="M18 20l10 11M34 15l10 11M50 11l10 11" stroke="var(--producers)" stroke-width="5"/><rect x="6" y="40" width="68" height="34" fill="#fff"/><rect x="6" y="46" width="68" height="4" fill="var(--producers)"/></svg><span class="tile-label">Producers</span></a>
    <a class="tile" href="#" style="left:811px;top:224px;background:var(--years)"><svg viewBox="0 0 80 80"><rect x="4" y="4" width="72" height="8" fill="#fff"/><path d="M4 12h18c0 22 4 40 10 58H4z" fill="#fff"/><path d="M76 12H58c0 22-4 40-10 58h28z" fill="#fff"/><path d="M32 70l8-26 8 26z" fill="#fff" opacity=".3"/></svg><span class="tile-label">Release Years</span></a>
    <a class="tile" href="#" style="left:1007px;top:224px;background:var(--playlists)"><svg viewBox="0 0 80 80"><circle cx="40" cy="40" r="36" fill="#fff"/><circle cx="40" cy="40" r="31" fill="none" stroke="var(--playlists)" stroke-width="2"/><path d="M22 30a22 22 0 0 1 12-12M58 50a22 22 0 0 1-12 12" stroke="var(--playlists)" stroke-width="3" fill="none"/><circle cx="40" cy="40" r="10" fill="var(--playlists)"/><circle cx="40" cy="40" r="4" fill="#fff"/></svg><span class="tile-label">Playlists</span></a>

    <a class="tile" href="#" style="left:30px;top:418px;background:var(--online)"><svg viewBox="0 0 80 80"><rect x="4" y="8" width="72" height="50" fill="#fff"/><rect x="10" y="14" width="60" height="38" fill="var(--online)"/><rect x="34" y="58" width="12" height="10" fill="#fff"/><rect x="22" y="68" width="36" height="6" fill="#fff"/><path d="M34 24l14 9-14 9z" fill="#fff"/></svg><span class="tile-label">Online</span></a>
  </main>

  <div class="scrollbar"><div class="scrollbar-thumb"></div></div>
</div>
</body>
</html>
```